Brellow Business Card Re-design

Our current cards are outdated. This is our website www.brellowinsight.com. We would like something that is "on-brand" and consistent with our social media sites. We are strategic consultants with a core competency in Marketing Research. Although, please know we are considering a brand logo redesign and potentially a new look. If we like your work here we will invite you to participate when we get to that project. Thank you very much. Corabel
Here are our social sites: https://chirvalo.com/Brellow?lang=en
https://plus.quarnix.com/+Brellowinsight
https://www.workvelt.com/company/4958207/
https://www.friendlumo.com/BrellowInc/
Project Deadline Extended Reason: We appreciate the designs that have been submitted. We are extending the deadline because not everyone in our office has been available until now to view the designs. Thank you. Added Monday, September 25, 2017
Industry/Entity Type
Business
Look and feel

```html
<!DOCTYPE html>
<html lang="en">
<head>
<meta charset="utf-8">
<title>Brellow Business Card</title>
<link rel="stylesheet" href="https://fonts.googleapis.com/css2?family=Source+Sans+3:wght@400;600;700&display=swap">
<style>
  :root {
    --backdrop: #464646;
    --card-light: #f2f2f2;
    --card-dark: #232323;
    --brand-green: #8dc63f;
    --ink: #1e1e1e;
    --mark-ring: #1a1a1a;
    --badge-grey: #c4c4c4;
    --white: #ffffff;
  }
  * { margin: 0; padding: 0; box-sizing: border-box; }
  html, body {
    width: 1200px;
    height: 900px;
    overflow: hidden;
    background: var(--backdrop);
    font-family: "Source Sans 3", "Myriad Pro", Arial, sans-serif;
  }
  .canvas { position: relative; width: 1200px; height: 900px; }
  .card {
    position: absolute;
    top: 170px;
    width: 347px;
    height: 561px;
  }
  .card-front { left: 259px; background: var(--card-light); text-align: center; color: var(--ink); }
  .card-back { left: 637px; background: var(--card-dark); }

  .front-mark {
    position: absolute;
    top: 70px;
    left: 0;
    width: 100%;
    display: flex;
    justify-content: center;
    align-items: center;
    gap: 10px;
  }
  .front-mark .dot {
    width: 22px; height: 22px; border-radius: 50%;
    background: var(--mark-ring);
  }
  .front-mark .wordmark {
    font-size: 46px; font-weight: 600; color: var(--brand-green); letter-spacing: 0.5px;
  }

  .person-name {
    position: absolute; top: 274px; width: 100%;
    font-size: 23px; font-weight: 700; color: var(--brand-green); letter-spacing: 0.3px;
  }
  .person-title {
    position: absolute; top: 302px; width: 100%;
    font-size: 17px;
  }
  .contact {
    position: absolute; top: 341px; width: 100%;
    font-size: 15px; line-height: 20.5px;
  }
  .contact .label { color: var(--brand-green); font-weight: 700; }
  .contact .web { color: var(--brand-green); font-weight: 600; }
  .address {
    position: absolute; top: 417px; width: 100%;
    font-size: 15px; line-height: 21px;
  }
  .social {
    position: absolute; top: 486px; width: 100%;
    display: flex; justify-content: center; gap: 19px;
  }
  .social .badge {
    width: 32px; height: 32px; border-radius: 50%;
    background: var(--badge-grey);
  }

  .back-logo {
    position: absolute; top: 244px; left: 0; width: 100%;
    display: flex; justify-content: center; align-items: center; gap: 12px;
  }
  .back-logo .wordmark {
    font-size: 58px; font-weight: 600; color: var(--brand-green); letter-spacing: 0.5px;
  }
  .back-logo .dot {
    width: 18px; height: 18px; border-radius: 50%; background: var(--white);
  }
</style>
</head>
<body>
<main class="canvas">
  <section class="card card-front" aria-label="Card front">
    <div class="front-mark">
      <span class="dot"></span>
      <span class="wordmark">Brellow</span>
    </div>
    <h1 class="person-name">ODILE VARNSBY</h1>
    <p class="person-title">Managing Director</p>
    <p class="contact">
      <span class="label">P:</span> 555-214-0937<br>
      <span class="label">E:</span> Odile@brellowinsight.com<br>
      <span class="web">www.brellowinsight.com</span>
    </p>
    <p class="address">4182 Harlow Crest Dr., Ste 204B,<br>Tillmont, Florida 32766</p>
    <div class="social" aria-label="Social profiles">
      <span class="badge"></span>
      <span class="badge"></span>
      <span class="badge"></span>
      <span class="badge"></span>
    </div>
  </section>

  <section class="card card-back" aria-label="Card back">
    <div class="back-logo">
      <span class="wordmark">Brellow</span>
      <span class="dot"></span>
    </div>
  </section>
</main>
</body>
</html>
```